Website design for Harbor Bolts. ( Lock company)

Harbor Bolts is a New York Based Company that manufactures a variety of high quality Locks which sell worldwide.

Our website: We need a 'face' on the Internet , a website that tells you who we are and what we do - 'An Identity'.

it is not an eCommerce website . the website is to show customers and potential distributers who we are and what we manufacture ( so they come away with a great impression of our company and our products) see www.quarrelwheel.com

First glance impression: We are Professional; are locks are strong,and reliable. and we are ready to compete with other major Lock companies

Content: for starters the site will contain general information and background about our company (our story), were to buy our products, contact information, and display images of our Locks (and of course all the classic links including to all the legal and technical information). as time goes on we will add more features to the website i.e. Products, Videos blogs etc.

although at first there will not be that much content on the website - it should not look empty (it should be simple and clear but not empty) it should look and feel like a full fledged professional website (not a template)

Inspiration: here are a few sites which have the feel we are looking for:

General tone - quarrelwheel.com bramhold.com (black is good - But not a must )

Simplicity, clarity - coldvane.com panwright.com

the widescreen Image look - http://www.pagecritter.com/demo/58261.html

we are considering perhaps having wide HQ images of Lion(s) in the background (but without the felling that it is a zoo or safari website) - it is not a must, its just an idea .

perhaps (if you find it looks good ) use a bit of that metal or chrome look to give it it a strong smooth feel (however it should not look like a dark prison)

We do not currently have a Logo ( if you feel you can design one that fits the above company description - we would love to see if it can work for us) We can talk about additional funds for the logo during this project.

Our working slogan is : Harbor Bolts - "Keeper of your Ground"

for your convenience we have attached a few images of the type of locks we sell

We are looking to collaborate with you throughout the project. We have ideas and visions we want implemented and we will help you along the way. So we can create the perfect website.

Thank you.

```html
<!DOCTYPE html>
<html lang="en">
<head>
<meta charset="utf-8">
<title>Harbor Bolts – Keeper of your Ground</title>
<link rel="stylesheet" href="https://fonts.googleapis.com/css2?family=Lato:wght@400;700;900&family=Oswald:wght@400;600&display=swap">
<style>
:root{
  --page:#262626;
  --page-dark:#1b1b1b;
  --panel:#323232;
  --panel-line:#3e3e3e;
  --red:#d62a2a;
  --red-dark:#a81d1d;
  --text:#bdbdbd;
  --muted:#8a8a8a;
  --white:#ffffff;
  --black:#0c0c0c;
}
*{box-sizing:border-box;margin:0;padding:0}
html,body{width:822px;height:1200px;overflow:hidden}
body{background:var(--page);font-family:"Lato",Arial,sans-serif;color:var(--text);font-size:9px;line-height:1.5}
.wrap{width:628px;margin:0 auto;position:relative}

/* header */
.site-header{height:60px;background:var(--page-dark)}
.site-header .wrap{display:flex;justify-content:space-between;align-items:center;height:60px}
.brand-name{font-family:"Oswald",sans-serif;font-weight:600;font-size:22px;color:var(--red);line-height:1}
.brand-slogan{font-size:9px;color:var(--muted);margin-top:3px}
.header-tools{display:flex;align-items:center;gap:10px;font-size:9px;color:var(--white)}
.header-tools .sep{color:var(--muted)}
.search{display:flex;margin-left:8px}
.search-input{width:150px;height:18px;background:var(--white);border:0}
.search-btn{width:50px;height:18px;background:var(--red);color:var(--white);font-size:9px;display:flex;align-items:center;justify-content:center;font-weight:700}

/* nav */
.main-nav{background:linear-gradient(var(--red),var(--red-dark));height:26px;margin-top:2px}
.main-nav ul{list-style:none;display:flex;height:26px}
.main-nav li{flex:1;text-align:center;line-height:26px;color:var(--white);font-size:10px;border-right:1px solid rgba(0,0,0,.2)}
.main-nav li:last-child{border-right:0}

/* hero */
.hero{margin-top:16px;height:268px;background:var(--panel);border:1px solid var(--panel-line);display:flex;padding:12px;gap:16px}
.hero-media{width:318px;height:242px;position:relative;background:radial-gradient(circle at 45% 45%,#f2f2f2,#c9c9c9 70%,#9e9e9e);border-radius:2px}
.hero-dots{position:absolute;bottom:10px;left:50%;transform:translateX(-50%);display:flex;gap:6px}
.hero-dots span{width:8px;height:8px;border-radius:50%;background:#777}
.hero-dots span.active{background:var(--red)}
.hero-copy{flex:1;padding-top:14px;position:relative}
.hero-title{font-size:26px;font-weight:900;color:var(--white);line-height:1.1;margin-bottom:16px}
.hero-list{list-style:none}
.hero-list li{display:flex;align-items:center;gap:10px;font-size:10px;color:var(--white);padding:6px 0}
.hero-list svg{flex:none}
.btn-red{background:var(--red);color:var(--white);font-weight:700;font-size:10px;padding:5px 10px;display:inline-block}
.hero-copy .btn-red{position:absolute;right:0;bottom:0}

/* info panels */
.duo{display:flex;gap:14px;margin-top:14px}
.panel{flex:1;background:var(--panel);border:1px solid var(--panel-line);padding:12px 14px;height:164px;overflow:hidden}
.section-title{font-family:"Oswald",sans-serif;font-weight:400;font-size:15px;color:var(--red);padding-bottom:6px;border-bottom:1px solid var(--panel-line);margin-bottom:8px}
.panel p{font-size:8px;color:var(--muted);margin-bottom:8px}
.dealer-grid{display:flex;flex-wrap:nowrap;justify-content:space-between;margin-top:6px}
.dealer-badge{width:36px;height:32px;background:#474747;border:1px solid #555;display:flex;align-items:center;justify-content:center;flex:none}
.dealer-badge span{width:15px;height:15px;background:var(--red)}

/* products band */
.products{margin-top:14px;background:var(--black);height:218px;display:flex;align-items:center}
.products .wrap{display:flex;align-items:center;gap:10px}
.arrow{width:14px;height:40px;background:#2b2b2b;display:flex;align-items:center;justify-content:center;flex:none}
.product-row{display:flex;gap:10px;flex:1}
.product-card{flex:1;background:#2c2c2c;border:1px solid #444;padding:6px;height:170px;display:flex;flex-direction:column}
.product-image{flex:1;background:radial-gradient(circle,#ffffff,#d4d4d4 75%)}
.product-name{font-size:9px;font-weight:700;color:var(--white);text-align:center;margin-top:6px}
.product-note{font-size:7px;color:var(--muted);text-align:center}

/* general info */
.general{margin-top:16px;background:var(--panel);border:1px solid var(--panel-line);padding:12px 14px;height:150px}
.general p{font-size:8px;color:var(--muted);margin-bottom:10px}

/* footer */
.site-footer{margin-top:16px;background:var(--page-dark);height:236px}
.site-footer .wrap{display:flex;gap:24px;padding-top:18px}
.footer-col{flex:1}
.footer-col h4{font-size:10px;color:var(--white);font-weight:700;border-bottom:1px solid var(--panel-line);padding-bottom:5px;margin-bottom:6px}
.footer-col ul{list-style:none}
.footer-col li{font-size:8px;color:var(--muted);padding:3px 0;border-bottom:1px dotted #333}
.footer-col p{font-size:8px;color:var(--muted);padding:2px 0}
.newsletter-title{color:var(--white)!important;font-weight:700;font-size:10px!important;margin-top:8px}
.newsletter-input{height:18px;background:var(--white);color:#777;font-size:8px;padding:0 6px;line-height:18px;margin-top:4px}
.newsletter-submit{display:inline-block;background:var(--red);color:var(--white);font-weight:700;font-size:9px;padding:3px 14px;margin-top:8px;float:right}
.legal{width:628px;margin:14px auto 0;border-top:1px solid var(--panel-line);padding-top:8px;font-size:8px;color:var(--muted)}
</style>
</head>
<body>

<header class="site-header">
  <div class="wrap">
    <div class="brand">
      <div class="brand-name">Harbor Bolts</div>
      <div class="brand-slogan">Keeper of your Ground</div>
    </div>
    <div class="header-tools">
      <span>Where to Buy</span><span class="sep">|</span><span>Wish List</span>
      <div class="search"><div class="search-input"></div><div class="search-btn">Search</div></div>
    </div>
  </div>
</header>

<nav class="main-nav wrap">
  <ul>
    <li>Home</li><li>Products</li><li>Smart Security</li><li>How To Choose</li><li>Trade Resources</li><li>About Us</li><li>Contact Us</li>
  </ul>
</nav>

<section class="hero wrap">
  <div class="hero-media" role="img" aria-label="Photo of chrome padlocks and a keyed deadbolt">
    <div class="hero-dots"><span class="active"></span><span></span><span></span><span></span></div>
  </div>
  <div class="hero-copy">
    <h1 class="hero-title">Key Control Deadbolt</h1>
    <ul class="hero-list">
      <li><svg width="10" height="10" viewBox="0 0 10 10"><path d="M3 1l4 4-4 4" stroke="#fff" stroke-width="1.6" fill="none"/></svg>Lorem Ipsum is simply dummy text of the printing</li>
      <li><svg width="10" height="10" viewBox="0 0 10 10"><path d="M3 1l4 4-4 4" stroke="#fff" stroke-width="1.6" fill="none"/></svg>Dummy text of the printing and typesetting</li>
      <li><svg width="10" height="10" viewBox="0 0 10 10"><path d="M3 1l4 4-4 4" stroke="#fff" stroke-width="1.6" fill="none"/></svg>Simply dummy text of the printing and typesetting industry</li>
      <li><svg width="10" height="10" viewBox="0 0 10 10"><path d="M3 1l4 4-4 4" stroke="#fff" stroke-width="1.6" fill="none"/></svg>Ipsum is simply dummy text of the printing and typesetting.</li>
    </ul>
    <span class="btn-red">Read More</span>
  </div>
</section>

<div class="duo wrap">
  <section class="panel">
    <h2 class="section-title">Our Story</h2>
    <p>Lorem Ipsum is simply dummy text of the printing and typesetting industry. Lorem Ipsum has been the industry's standard dummy text ever since the 1500s, when an unknown printer took a galley of type and scrambled it to make a type specimen book.</p>
    <p>It has survived not only five centuries, but also the leap into electronic typesetting, remaining essentially unchanged. It was popularised in the 1960s with the release of Letraset sheets containing passages.</p>
  </section>
  <section class="panel">
    <h2 class="section-title">Were to Buy Our Products</h2>
    <p>Lorem Ipsum is simply dummy text of the printing and typesetting industry. Lorem Ipsum has been the industry's standard dummy text ever since the 1500s, when an unknown printer.</p>
    <div class="dealer-grid">
      <div class="dealer-badge"><span></span></div><div class="dealer-badge"><span></span></div><div class="dealer-badge"><span></span></div>
      <div class="dealer-badge"><span></span></div><div class="dealer-badge"><span></span></div><div class="dealer-badge"><span></span></div>
    </div>
  </section>
</div>

<section class="products">
  <div class="wrap">
    <div class="arrow"><svg width="8" height="12" viewBox="0 0 8 12"><path d="M6 1L2 6l4 5" stroke="#fff" stroke-width="1.6" fill="none"/></svg></div>
    <div class="product-row">
      <div class="product-card"><div class="product-image" role="img" aria-label="Brass knob deadbolt set"></div><div class="product-name">Lorem Ipsum Simply</div><div class="product-note">Dummy text of the printing</div></div>
      <div class="product-card"><div class="product-image" role="img" aria-label="Black combination padlock"></div><div class="product-name">Lorem Ipsum Simply</div><div class="product-note">Dummy text of the printing</div></div>
      <div class="product-card"><div class="product-image" role="img" aria-label="Brass door knob lockset"></div><div class="product-name">Lorem Ipsum Simply</div><div class="product-note">Dummy text of the printing</div></div>
      <div class="product-card"><div class="product-image" role="img" aria-label="Brass keyed deadbolt"></div><div class="product-name">Lorem Ipsum Simply</div><div class="product-note">Dummy text of the printing</div></div>
      <div class="product-card"><div class="product-image" role="img" aria-label="Blue and chrome padlock"></div><div class="product-name">Lorem Ipsum Simply</div><div class="product-note">Dummy text of the printing</div></div>
    </div>
    <div class="arrow"><svg width="8" height="12" viewBox="0 0 8 12"><path d="M2 1l4 5-4 5" stroke="#fff" stroke-width="1.6" fill="none"/></svg></div>
  </div>
</section>

<section class="general wrap">
  <h2 class="section-title">General Information</h2>
  <p>Lorem Ipsum is simply dummy text of the printing and typesetting industry. Lorem Ipsum has been the industry's standard dummy text ever since the 1500s, when an unknown printer took a galley of type and scrambled it to make a type specimen book. It has survived not only five centuries.</p>
  <p>It has survived not only five centuries, but also the leap into electronic typesetting, remaining essentially unchanged. It was popularised in the 1960s with the release of Letraset sheets containing Lorem Ipsum passages, and more recently with desktop publishing software.</p>
</section>

<footer class="site-footer">
  <div class="wrap">
    <div class="footer-col">
      <h4>Site Link</h4>
      <ul><li>Products</li><li>Smart Security</li><li>How to Choose</li><li>Trade Resources</li></ul>
    </div>
    <div class="footer-col">
      <h4>Support Tools</h4>
      <ul><li>Where to Buy</li><li>Wish List</li><li>Installation Guides</li><li>Warranty</li></ul>
    </div>
    <div class="footer-col">
      <h4>Contact Information</h4>
      <p>Toll Free: 1-800-555-0142</p>
      <p>Email: hello@harborbolts.example</p>
      <p class="newsletter-title">Newsletter</p>
      <div class="newsletter-input">Enter your E-mail</div>
      <span class="newsletter-submit">Submit</span>
    </div>
  </div>
  <div class="legal">© 2013 Harbor Bolts. All rights reserved. · Legal and Technical Information</div>
</footer>

</body>
</html>
```